Conservative, Modern and Sharp Builder Business card

Hi there,
We would like to update our existing business card.
I have attached photos of existing business card, logo and van sign.

I would like the business card to also list what we do :
Renovation • New Build • Alteration
Extension • Bathroom • Maintenance.(Seperated by dots)

Contact number : 021 0483 0752
(With that exact spacing)

Ideally when people looking from about 2-3 metres, they know that it is a builder’s business card

Open to suggestions on fonts, layout, style of business card

PLEASE ONLY SUBMIT YOUR BEST OR MAX 3 DESIGNS FOR EACH DESIGNER

Thanks

Industry/Entity Type

Construction. Renovation

Contact Information for Business Card

Details should be the same as the existing card. And addition of what we do.

Requirements
Should not have
• The new business card must not have the same layout as our existing one. Thanks

```html
<!DOCTYPE html>
<html lang="en">
<head>
<meta charset="utf-8">
<title>Kestrel Homes Business Card</title>
<link href="https://fonts.googleapis.com/css2?family=Inter:wght@400;600;700&display=swap" rel="stylesheet">
<style>
  :root {
    --backdrop: #9b9b9b;
    --card-dark: #111111;
    --card-light: #ffffff;
    --ink: #111111;
    --ink-soft: #4a4a4a;
    --ink-reverse: #ececec;
  }
  * { margin: 0; padding: 0; box-sizing: border-box; }
  html, body {
    width: 1200px; height: 588px; overflow: hidden;
    background: var(--backdrop);
    font-family: "Inter", Arial, sans-serif;
  }
  .canvas { position: relative; width: 1200px; height: 588px; }
  .card {
    position: absolute; top: 142px;
    width: 487px; height: 287px;
  }
  .card--front { left: 87px; background: var(--card-dark); }
  .card--back { left: 622px; background: var(--card-light); color: var(--ink); }

  .front-brand {
    position: absolute; left: 0; right: 0; top: 118px;
    text-align: center;
    color: var(--ink-reverse); font-weight: 700; font-size: 42px;
    letter-spacing: -0.8px; line-height: 1;
  }

  .back-brand {
    position: absolute; right: 21px; top: 90px;
    font-weight: 700; font-size: 34px; letter-spacing: -0.7px; line-height: 1;
  }

  .person { position: absolute; left: 20px; top: 132px; }
  .person-name { font-weight: 700; font-size: 17px; letter-spacing: 0.2px; line-height: 1.2; }
  .person-role { font-size: 12.5px; color: var(--ink-soft); margin-top: 2px; }

  .divider {
    position: absolute; left: 21px; right: 21px; top: 180px;
    height: 1px; background: var(--ink);
  }

  .contacts { position: absolute; left: 22px; top: 193px; list-style: none; }
  .contacts li {
    display: flex; align-items: center; gap: 7px;
    height: 18.4px; font-size: 12.5px; color: var(--ink-soft);
  }
  .contacts li.phone { color: var(--ink); font-weight: 600; font-size: 13.5px; }
  .contacts svg { width: 10px; height: 10px; flex: none; fill: var(--ink); }

  .services {
    position: absolute; right: 21px; top: 230px;
    text-align: right; font-size: 12.5px; color: var(--ink-soft); line-height: 18.4px;
  }
</style>
</head>
<body>
<div class="canvas">
  <section class="card card--front">
    <div class="front-brand">Kestrel Homes</div>
  </section>

  <section class="card card--back">
    <div class="back-brand">Kestrel Homes</div>

    <div class="person">
      <div class="person-name">TOMAS REIHANA</div>
      <div class="person-role">Residential Builder</div>
    </div>

    <div class="divider"></div>

    <ul class="contacts">
      <li class="phone">
        <svg viewBox="0 0 24 24"><path d="M6.6 10.8a15.1 15.1 0 0 0 6.6 6.6l2.2-2.2c.3-.3.7-.4 1-.2 1.1.4 2.3.6 3.6.6.6 0 1 .4 1 1V20c0 .6-.4 1-1 1C10.6 21 3 13.4 3 4c0-.6.4-1 1-1h3.5c.6 0 1 .4 1 1 0 1.3.2 2.5.6 3.6.1.3 0 .7-.2 1z"/></svg>
        021 0483 0752
      </li>
      <li>
        <svg viewBox="0 0 24 24"><path d="M2 5h20v14H2z"/><path d="M3 6l9 6.3L21 6" stroke="#fff" stroke-width="1.6" fill="none"/></svg>
        hello@kestrelhomes.co.nz
      </li>
      <li>
        <svg viewBox="0 0 24 24"><circle cx="12" cy="12" r="10"/><path d="M2 12h20M12 2c3 3 3 17 0 20M12 2c-3 3-3 17 0 20" stroke="#fff" stroke-width="1.4" fill="none"/></svg>
        www.KestrelHomes.co.nz
      </li>
      <li>
        <svg viewBox="0 0 24 24"><circle cx="12" cy="12" r="8"/></svg>
        KestrelHomes.nz
      </li>
    </ul>

    <div class="services">
      Renovation • New Build • Alteration<br>
      Extension • Bathroom • Maintenance
    </div>
  </section>
</div>
</body>
</html>
```